New website for engineering consultant

We need to update our existing web site. We've just had our logo re-done and have attached it.

We are an engineering consulting firm that specialises in mechanical and structural engineering, design and drafting. Our customers are other businesses in the manufacturing, mining and agricultural industries.

We would like the designs to be professional and highlight that we are innovative.

Industry/Entity Type

Mining

Requirements
Must have
• A module that rotates pictures so we can showcase certain projects. We have attached a few rendered images of projects for you to play with.

```html
<!DOCTYPE html>
<html lang="en">
<head>
<meta charset="utf-8">
<title>KOR-TECH PTY LTD – Mechanical Engineering and Technology</title>
<link href="https://fonts.googleapis.com/css2?family=Arimo:ital,wght@0,400;0,700;1,400&family=EB+Garamond&family=Open+Sans&display=swap" rel="stylesheet">
<style>
:root{
  --white:#ffffff;
  --hero-grey:#e6e6e6;
  --tab-grey:#a9a9a9;
  --social-grey:#cdcdcd;
  --navy:#1b2747;
  --navy-deep:#17223f;
  --brand-blue:#4a64a8;
  --nav-blue:#3b5a9d;
  --slogan-blue:#5868a6;
  --panel-slate:#6677a6;
  --panel-blue:#2b4f9d;
  --tab-yellow:#e2a91f;
  --tab-orange:#e27a38;
  --text-dark:#222;
  --text-mid:#666;
  --footer-text:#4c5c8c;
}
*{margin:0;padding:0;box-sizing:border-box}
html,body{width:1200px;height:1000px;overflow:hidden;background:var(--white)}
body{position:relative;font-family:"Arimo",Arial,sans-serif;color:var(--text-dark)}
.abs{position:absolute}

.brand{left:157px;top:38px;display:flex;align-items:center;gap:14px}
.brand-mark{width:58px;height:58px;border-radius:50%;background:var(--brand-blue)}
.brand-name{font-weight:700;font-size:25px;color:var(--brand-blue);letter-spacing:-.5px}
.brand-suffix{font-size:10px;letter-spacing:0}

.social{left:868px;top:28px;display:flex;gap:8px}
.social span{width:24px;height:24px;border-radius:50%;background:var(--social-grey)}

.main-nav{left:159px;top:126px;display:flex;gap:9px;font-size:12px}
.main-nav a{color:var(--nav-blue);text-decoration:none}

.call-tab{left:828px;top:106px;width:256px;height:43px}
.call-text{left:906px;top:120px;color:var(--white);font-style:italic;font-size:14px}

.hero{left:0;top:149px;width:1200px;height:292px;background:var(--hero-grey)}
.hero-photo{left:105px;top:149px;width:533px;height:292px}
.slogan{left:682px;top:196px;font-family:"EB Garamond",Georgia,serif;font-size:31px;color:var(--slogan-blue)}
.tagline{left:684px;top:237px;width:300px;font-family:"Open Sans",Arial,sans-serif;font-size:16px;line-height:20px;color:var(--text-mid)}
.intro-box{left:679px;top:287px;width:336px;height:44px;border-radius:7px;background:#d3d3d3;padding:7px 16px;font-size:9.5px;line-height:14px;font-style:italic;color:#777}
.cta{left:679px;top:344px;width:125px;height:33px;border-radius:17px;background:linear-gradient(#7f8dc0,#4e5e98);color:var(--white);font-size:12.5px;text-align:center;line-height:33px;box-shadow:0 2px 3px rgba(0,0,0,.3)}

.band{left:0;top:441px;width:1200px;height:144px;background:linear-gradient(135deg,var(--navy),#243258)}

.panel{top:551px;height:106px;color:var(--white);font-weight:700;font-size:12px;line-height:18px;padding:17px 0 0 27px}
.panel-improve{left:142px;width:229px;background:var(--panel-slate)}
.panel-projects{left:371px;width:230px;background:var(--panel-blue)}
.corner{top:551px;width:35px;height:34px}
.corner-yellow{left:107px;background:var(--tab-yellow)}
.corner-orange{left:337px;width:34px;background:var(--tab-orange)}
.tab-label{top:532px;color:var(--white);font-size:12px}

.slider{left:625px;top:418px;width:429px;height:240px;background:var(--white);box-shadow:0 1px 6px rgba(0,0,0,.3)}
.slide{left:12px;top:13px;width:405px;height:214px;background:linear-gradient(160deg,#6d6f6a,#c9cac6 55%,#f2f2f2)}
.latest-tab{left:795px;top:658px;width:237px;height:35px}
.latest-text{left:827px;top:670px;color:var(--white);font-size:11.5px}
.dots{left:928px;top:671px;display:flex;gap:5px}
.dots span{width:12px;height:12px;border-radius:50%;background:#eee;border:1px solid #888}

.about{left:145px;top:697px;width:540px;font-size:11.6px;line-height:18px;text-align:justify}
.about p+p{margin-top:18px}

.clients-area{left:0;top:0;width:1200px;height:1000px}
.client-name{top:808px;font-size:26px;font-weight:700;color:#b8b8b8}
.clients-label{left:920px;top:889px;color:var(--white);font-size:14px}
.copyright{left:764px;top:951px;color:var(--footer-text);font-size:12px;line-height:18px}
</style>
</head>
<body>

<div class="abs brand"><span class="brand-mark"></span><span class="brand-name">KOR-TECH <span class="brand-suffix">PTY LTD</span></span></div>

<div class="abs social" aria-label="Social links"><span></span><span></span><span></span><span></span><span></span><span></span></div>

<nav class="abs main-nav">
  <a href="#">Home</a><a href="#">About us</a><a href="#">Engineering and design</a><a href="#">Technology</a><a href="#">Speciality Services</a><a href="#">Contact us</a>
</nav>

<svg class="abs call-tab" viewBox="0 0 256 43">
  <polygon points="14,0 256,0 242,43 0,43" fill="var(--tab-grey)"/>
  <circle cx="55" cy="22" r="12" fill="none" stroke="#555" stroke-width="1.5"/>
  <path d="M50 16 q-2 3 1 8 q3 5 8 5 l2-3 -3-2 -2 1.5 q-3-1 -4-5 l1.5-2 -2-3z" fill="#555"/>
</svg>
<div class="abs call-text">Call us (07) 4000 1234</div>

<div class="abs hero"></div>
<svg class="abs hero-photo" viewBox="0 0 533 292" role="img" aria-label="Engineer in a hard hat reviewing plans in a steel-framed workshop">
  <defs><linearGradient id="photoTone" x1="0" y1="0" x2="1" y2="1"><stop offset="0" stop-color="#c9cbcf"/><stop offset="1" stop-color="#8d949e"/></linearGradient></defs>
  <polygon points="43,0 533,0 498,292 0,292" fill="var(--white)"/>
  <polygon points="47,0 524,0 490,292 8,292" fill="url(#photoTone)"/>
</svg>

<div class="abs slogan">NICE SLOGAN HERE</div>
<div class="abs tagline">We are mechanical engineering and technology company</div>
<div class="abs intro-box">Lorem ipsum dolor sit amet, consectetur adipiscing elit. Aliquam molestie massa in erat porta id luctus arcu sollicitudin. Fusce elit</div>
<div class="abs cta">Find out more</div>

<div class="abs band"></div>

<svg class="abs" style="left:150px;top:523px" width="416" height="28">
  <polygon points="10,0 194,0 184,28 0,28" fill="var(--tab-yellow)"/>
  <polygon points="231,0 415,0 405,28 221,28" fill="var(--tab-orange)"/>
</svg>
<div class="abs tab-label" style="left:175px">IMPROVEMENT SEVICES</div>
<div class="abs tab-label" style="left:400px">PROJECTS</div>

<div class="abs panel panel-improve">KOR-TECH believes in the philosophy of Lean Thinking as promoted by Velornis with their Velornis Production System...</div>
<div class="abs panel panel-projects">Lorem ipsum dolor sit amet, consectetur adipiscing elit. Aliquam molestie massa in erat porta id luctus arcu velit,...</div>
<div class="abs corner corner-yellow"></div>
<div class="abs corner corner-orange"></div>

<div class="abs slider">
  <div class="abs slide" role="img" aria-label="Rendered steel bull bar project"></div>
</div>
<svg class="abs latest-tab" viewBox="0 0 237 35"><polygon points="12,0 237,0 225,35 0,35" fill="var(--tab-grey)"/></svg>
<div class="abs latest-text">LATEST WORK</div>
<div class="abs dots"><span></span><span></span><span></span><span></span></div>

<div class="abs about">
  <p>KOR-TECH is a mechanical engineering and technology company focused on helping local manufacturing companies and local industries improve their products, services and sustainability through the application of engineering, technology and focused improvement.</p>
  <p>We offer a broad range of services that are designed to support and nurture manufacturing companies and industries whether you are big or small. We bring togther the services you would only find in a capital city to companies in North Queensland at a competitive rates. Our core services revolve around the application of the latest 3D Solid Modelling technology to assist in creating solutions to your mechanical design problems. These services are complemented by our Technology services which are designed to help your company leverage the latest technology to become globally competitive. Furthermore we offer a range of Focused Improvement and Specialty services as we strive to bring you complete solutions to your business.</p>
</div>

<svg class="abs clients-area" viewBox="0 0 1200 1000">
  <polygon points="790,715 1200,715 1200,985 735,985" fill="var(--navy)"/>
  <rect x="0" y="985" width="1200" height="15" fill="var(--navy-deep)"/>
  <polygon points="715,772 1047,772 990,880 715,880" fill="var(--white)"/>
  <circle cx="1016" cy="826" r="22" fill="var(--panel-blue)"/>
  <path d="M1008 818 l8 8 -8 8 M1016 818 l8 8 -8 8" stroke="var(--white)" stroke-width="2.5" fill="none"/>
</svg>
<div class="abs client-name" style="left:755px">Vantrell</div>
<div class="abs client-name" style="left:870px">Brakon</div>
<div class="abs clients-label">Our clients</div>
<div class="abs copyright">Copyright © 2009 KOR-TECH PTY LTD<br>All Rights Reserved.</div>

</body>
</html>
```